lithographic lamination design for Holiday gift box

We will use this design to produce full coverage lithographic labels we will laminate to Corrugated and then diecut. I have provided a .pdf file of the box with dimensions and sell sheet examples of our 5 business units. We would like the box to summarize the story of our company to our customer. It will house a tin of chocolate covered peanuts. We would like to include our contact info on the bottom panel of the box as well. Our salespeople will be handing these out to our customers.

Target Market(s)

business to business

Industry/Entity Type

Graphic Design

Colors

Designer to choose colors to be used in the design.

Requirements
Must have
• must represent all 5 of our business divisions and contain information on capabilities included on the sell sheets I provided. It must include our logo and contact info. We would like each of our divisions represented on the panels of the box and our contact info on the bottom panel. Corrugated is our primary business. Please keep this in mind and feature this. This is a graphic design. I do not need a box design. I have provided one.
Nice to have
• Utilize font the same as or complimentary to the fonts used on our sell sheets.

```html
<!DOCTYPE html>
<html lang="en">
<head>
<meta charset="utf-8">
<title>Norvale Holiday Gift Box – Panel Artwork</title>
<link href="https://fonts.googleapis.com/css2?family=Oswald:wght@500;600&family=Open+Sans:wght@400;600;700&display=swap" rel="stylesheet">
<style>
  :root{
    --bg:#6d6d6d;
    --orange:#f3a93a;
    --green:#7cbb43;
    --ink:#3b3b3b;
    --grey:#7d7d7d;
    --paper:#ffffff;
    --rule:rgba(255,255,255,.75);
  }
  *{box-sizing:border-box;margin:0;padding:0}
  html,body{width:1200px;height:3224px;overflow:hidden;background:var(--bg)}
  body{position:relative;font-family:"Open Sans",Arial,sans-serif;color:var(--ink)}

  .panel{position:absolute;width:540px;height:540px;background:var(--paper);overflow:hidden}
  .col-a{left:40px}.col-b{left:620px}
  .row-1{top:267px}.row-2{top:1342px}.row-3{top:2417px}

  .heading{font-family:"Oswald",Arial,sans-serif;font-weight:600;text-transform:uppercase;letter-spacing:1px}

  /* side panels: vertical title column */
  .side-title{position:absolute;left:18px;top:30px;bottom:40px;width:50px;display:flex;align-items:center;justify-content:center;
    writing-mode:vertical-rl;transform:rotate(180deg);font-size:38px;color:var(--ink);white-space:nowrap}

  .photo{position:absolute}
  .photo-corrugated{background:linear-gradient(180deg,#b98650 0%,#8f6036 55%,#6e4526 100%)}
  .photo-pallets{background:linear-gradient(160deg,#e0c196,#a97d4c)}
  .photo-supplies{background:linear-gradient(160deg,#2d2d2d,#5e5e5e 60%,#bdbdbd)}
  .photo-bags{background:linear-gradient(160deg,#f4f4f4,#c4c4c4)}
  .photo-transit{background:linear-gradient(180deg,#e9d6b4,#b68c57)}

  .stripe{position:absolute;left:0;right:0;bottom:0;height:10px;background:linear-gradient(90deg,var(--green),var(--orange))}

  .brand{position:absolute;right:20px;bottom:28px;display:flex;align-items:center;gap:10px;background:var(--paper);padding:8px 14px}
  .brand .mark{width:14px;height:14px;background:var(--orange)}
  .brand .name{font-family:"Oswald",Arial,sans-serif;font-weight:600;font-size:26px;color:var(--ink);letter-spacing:1px}

  /* tagged capability list */
  .tag-list{position:absolute;left:82px;top:36px;width:250px;list-style:none;display:flex;flex-direction:column;gap:22px}
  .tag-list .tag{display:inline-block;background:var(--orange);color:#fff;font-size:12px;font-weight:700;padding:2px 9px;text-transform:uppercase}
  .tag-list p{font-size:13px;color:var(--grey);margin-top:5px;line-height:1.4}

  /* tick list */
  .tick-list{position:absolute;left:84px;top:50px;width:190px;list-style:none;display:flex;flex-direction:column;gap:26px}
  .tick-list li{display:flex;align-items:center;gap:10px;font-size:15px;font-weight:600;color:var(--ink)}
  .tick-list svg{flex:none}

  /* corrugated top panel */
  .top-band{position:absolute;left:0;right:0;top:180px;bottom:0;background:var(--orange)}
  .top-title{position:absolute;left:36px;top:198px;font-size:32px;color:var(--paper)}
  .rule-list{position:absolute;left:36px;top:256px;width:360px;list-style:none}
  .rule-list li{border-bottom:1px solid var(--rule);padding:8px 0;font-size:13px;color:var(--ink)}
  .rule-list b{color:#fff;font-weight:700;margin-right:6px}

  /* bottom panel */
  .bottom{background:var(--orange)}
  .contact-card{position:absolute;left:40px;top:48px;width:300px;background:var(--paper);padding:20px 22px}
  .contact-card .name{font-family:"Oswald",Arial,sans-serif;font-weight:600;font-size:34px;letter-spacing:1px;display:flex;align-items:center;gap:10px;color:var(--ink)}
  .contact-card .name i{width:16px;height:16px;background:var(--orange);display:inline-block}
  .contact-card .phone{margin-top:10px;display:inline-block;background:var(--orange);color:#fff;font-weight:700;font-size:15px;padding:3px 10px}
  .contact-card p{font-size:12px;color:var(--grey);margin-top:8px;line-height:1.5}
  .divisions{position:absolute;left:40px;top:300px;width:460px;font-size:14px;color:var(--ink);line-height:1.6}
  .divisions h3{font-size:20px;color:#fff;margin-bottom:8px}
</style>
</head>
<body>

<!-- Top panel: Corrugated Products -->
<section class="panel col-a row-1">
  <div class="photo photo-corrugated" style="left:0;top:0;right:0;height:180px" role="img" aria-label="Photo of stacked corrugated board edges tied with a red holiday ribbon and bow"></div>
  <div class="top-band"></div>
  <h2 class="heading top-title">Corrugated Products</h2>
  <ul class="rule-list">
    <li><b>Custom Boxes</b>Built to fit every product</li>
    <li><b>Die Cut</b>Precise shapes, fast turns</li>
    <li><b>Litho Lamination</b>Full color retail graphics</li>
    <li><b>Displays</b>Point of purchase that sells</li>
    <li><b>Shipping Cartons</b>Strong stock, any quantity</li>
  </ul>
  <div class="brand"><span class="mark"></span><span class="name">NORVALE</span></div>
</section>

<!-- Side: Pallets -->
<section class="panel col-b row-1">
  <h2 class="heading side-title">Pallets</h2>
  <ul class="tag-list">
    <li><span class="tag">New Pallets</span><p>Built to your specs and delivered on your schedule.</p></li>
    <li><span class="tag">Recycled Pallets</span><p>Quality graded stock at a lower cost per load.</p></li>
    <li><span class="tag">Custom Sizes</span><p>Any footprint, deck or entry style you need.</p></li>
    <li><span class="tag">Heat Treated</span><p>Certified for export shipments worldwide.</p></li>
    <li><span class="tag">Pallet Retrieval</span><p>We collect, sort and recycle used pallets.</p></li>
  </ul>
  <div class="photo photo-pallets" style="right:0;top:0;width:180px;height:530px" role="img" aria-label="Photo of a stack of wooden pallets"></div>
  <div class="brand"><span class="mark"></span><span class="name">NORVALE</span></div>
  <div class="stripe"></div>
</section>

<!-- Side: Packaging Supplies -->
<section class="panel col-a row-2">
  <h2 class="heading side-title">Packaging Supplies</h2>
  <ul class="tick-list">
    <li><svg width="18" height="18" viewBox="0 0 18 18"><rect width="18" height="18" fill="#7cbb43"/><path d="M4 9l3 3 7-7" stroke="#fff" stroke-width="2.4" fill="none"/></svg>Stretch Film</li>
    <li><svg width="18" height="18" viewBox="0 0 18 18"><rect width="18" height="18" fill="#7cbb43"/><path d="M4 9l3 3 7-7" stroke="#fff" stroke-width="2.4" fill="none"/></svg>Tape &amp; Dispensers</li>
    <li><svg width="18" height="18" viewBox="0 0 18 18"><rect width="18" height="18" fill="#7cbb43"/><path d="M4 9l3 3 7-7" stroke="#fff" stroke-width="2.4" fill="none"/></svg>Void Fill</li>
    <li><svg width="18" height="18" viewBox="0 0 18 18"><rect width="18" height="18" fill="#7cbb43"/><path d="M4 9l3 3 7-7" stroke="#fff" stroke-width="2.4" fill="none"/></svg>Strapping</li>
    <li><svg width="18" height="18" viewBox="0 0 18 18"><rect width="18" height="18" fill="#7cbb43"/><path d="M4 9l3 3 7-7" stroke="#fff" stroke-width="2.4" fill="none"/></svg>Labels</li>
  </ul>
  <div class="photo photo-supplies" style="right:0;top:0;width:230px;height:530px" role="img" aria-label="Photo of a black shipping box with rolls of packing tape and stretch film"></div>
  <div class="stripe"></div>
</section>

<!-- Side: Bulk Bags -->
<section class="panel col-b row-2">
  <h2 class="heading side-title">Bulk Bags</h2>
  <ul class="tag-list">
    <li><span class="tag">Standard FIBCs</span><p>Stock sizes ready to ship the same week.</p></li>
    <li><span class="tag">Baffle Bags</span><p>Square fill that saves space in storage.</p></li>
    <li><span class="tag">Food Grade</span><p>Clean room made for sensitive products.</p></li>
    <li><span class="tag">Liners</span><p>Moisture barriers fitted to every bag.</p></li>
    <li><span class="tag">Discharge Spouts</span><p>Options for controlled, easy unloading.</p></li>
  </ul>
  <div class="photo photo-bags" style="right:0;top:0;width:180px;height:530px" role="img" aria-label="Photo of a white woven bulk bag with lifting loops"></div>
  <div class="brand"><span class="mark"></span><span class="name">NORVALE</span></div>
  <div class="stripe"></div>
</section>

<!-- Side: Transit Protection -->
<section class="panel col-a row-3">
  <h2 class="heading side-title">Transit Protection</h2>
  <ul class="tick-list">
    <li><svg width="18" height="18" viewBox="0 0 18 18"><rect width="18" height="18" fill="#7cbb43"/><path d="M4 9l3 3 7-7" stroke="#fff" stroke-width="2.4" fill="none"/></svg>Edge Protectors</li>
    <li><svg width="18" height="18" viewBox="0 0 18 18"><rect width="18" height="18" fill="#7cbb43"/><path d="M4 9l3 3 7-7" stroke="#fff" stroke-width="2.4" fill="none"/></svg>Dunnage Bags</li>
    <li><svg width="18" height="18" viewBox="0 0 18 18"><rect width="18" height="18" fill="#7cbb43"/><path d="M4 9l3 3 7-7" stroke="#fff" stroke-width="2.4" fill="none"/></svg>Load Locks</li>
    <li><svg width="18" height="18" viewBox="0 0 18 18"><rect width="18" height="18" fill="#7cbb43"/><path d="M4 9l3 3 7-7" stroke="#fff" stroke-width="2.4" fill="none"/></svg>Corner Boards</li>
    <li><svg width="18" height="18" viewBox="0 0 18 18"><rect width="18" height="18" fill="#7cbb43"/><path d="M4 9l3 3 7-7" stroke="#fff" stroke-width="2.4" fill="none"/></svg>Air Pillows</li>
  </ul>
  <div class="photo photo-transit" style="right:0;top:0;width:230px;height:530px" role="img" aria-label="Photo of a cardboard edge protector with strapping on a load"></div>
  <div class="stripe"></div>
</section>

<!-- Bottom panel: contact -->
<section class="panel bottom col-b row-3">
  <div class="contact-card">
    <div class="name"><i></i>NORVALE</div>
    <span class="phone">800.555.0142</span>
    <p>1200 Mill Road, Northfield, PA 17000<br>sales@norvalepack.com<br>www.norvalepack.com</p>
  </div>
  <div class="divisions">
    <h3 class="heading">One Partner, Five Divisions</h3>
    <p>Corrugated Products · Pallets · Packaging Supplies · Bulk Bags · Transit Protection. Thank you for your business and happy holidays from all of us.</p>
  </div>
</section>

</body>
</html>
```